Billboard design - consider what a billboard is

Design a billboard using my logo - Billboard is 6m x 3m
A Billboard is advertising for my company that is on a big sign.

Has to be clean and easy to read, and ideally highlights that we are Residential and Commercial builders.

Keep it clean and easy to read

The contact number for the board is

027 584 9071
www.fernridgebuildworks.co.nz
info@fernridgebuildworks.co.nz

Doesnt have to have all contact details if it doesnt fit

Has to catch peoples attention to contact us if they need a builder

Can you please change the sign to be all white writing, with black background ?
Updates

Please consider what a billboard is...

The design needs to be suitable for a billboard..

Target Market(s)

people driving past

Industry/Entity Type

Construction

Logo Text

Wellington Builder, website email address, contact number

Colors
0054AA
0677BA
7BADD7
CADEEF
E8F1F8

Requirements
Must have
• Easy to read
Nice to have
• easy to read, can clearly see contact details

```html
<!DOCTYPE html>
<html lang="en">
<head>
<meta charset="utf-8">
<title>Wellington Builder – Fernridge Buildworks Billboard</title>
<link rel="stylesheet" href="https://fonts.googleapis.com/css2?family=Orbitron:wght@500;700;900&family=Quicksand:wght@500&display=swap">
<style>
  :root {
    --ink: #000000;
    --paper: #ffffff;
    --sky: #6b96cf;
    --brand: #5a8ccb;
    --photo-site: #4f6a6e;
    --photo-site-dark: #2d3b40;
    --photo-home: #8fa7b8;
    --photo-home-light: #c9d4da;
    --badge: #0d1a2b;
  }
  html, body {
    margin: 0;
    padding: 0;
    width: 1200px;
    height: 600px;
    overflow: hidden;
    background: var(--ink);
  }
  .billboard {
    display: block;
    width: 1200px;
    height: 600px;
  }
  .headline {
    font-family: "Orbitron", sans-serif;
    font-weight: 900;
    fill: var(--paper);
  }
  .tagline {
    font-family: "Orbitron", sans-serif;
    font-weight: 500;
    fill: var(--paper);
  }
  .brand-name {
    font-family: "Orbitron", sans-serif;
    font-weight: 900;
    fill: var(--brand);
  }
  .phone-number {
    font-family: "Orbitron", sans-serif;
    font-weight: 700;
    fill: var(--paper);
  }
  .web-contact {
    font-family: "Quicksand", sans-serif;
    font-weight: 500;
    fill: var(--paper);
  }
  .icon-line {
    fill: none;
    stroke: var(--brand);
    stroke-linecap: round;
    stroke-linejoin: round;
  }
  .accent-band { fill: var(--sky); }
  .badge-mark { fill: var(--badge); }
</style>
</head>
<body>
<svg class="billboard" viewBox="0 0 1200 600" xmlns="http://www.w3.org/2000/svg">
  <defs>
    <linearGradient id="siteTone" x1="0" y1="0" x2="0" y2="1">
      <stop offset="0" stop-color="var(--photo-site)"/>
      <stop offset="1" stop-color="var(--photo-site-dark)"/>
    </linearGradient>
    <linearGradient id="homeTone" x1="0" y1="0" x2="0" y2="1">
      <stop offset="0" stop-color="var(--photo-home)"/>
      <stop offset="1" stop-color="var(--photo-home-light)"/>
    </linearGradient>
  </defs>

  <rect class="background" width="1200" height="600" fill="var(--ink)"/>

  <polygon class="accent-band" points="1180,0 1200,0 1200,600 985,600"/>

  <polygon class="project-photo main" role="img" aria-label="Aerial view of a townhouse development under construction with scaffolding and site fencing"
           points="717,0 1180,0 1071,321 608,321" fill="url(#siteTone)"/>
  <polygon class="project-photo" role="img" aria-label="Brick house with a new timber deck being built"
           points="589,339 744,339 694,484 550,484" fill="url(#homeTone)"/>
  <polygon class="project-photo" role="img" aria-label="Two-storey weatherboard house with white windows"
           points="758,339 904,339 852,484 709,484" fill="url(#homeTone)"/>
  <polygon class="project-photo" role="img" aria-label="Restored villa with a turret and cars parked on the street"
           points="918,339 1062,339 1011,484 867,484" fill="url(#homeTone)"/>

  <text class="headline" x="42" y="88" font-size="66" textLength="581" lengthAdjust="spacingAndGlyphs">WELLINGTON</text>
  <text class="headline" x="42" y="198" font-size="104" textLength="543" lengthAdjust="spacingAndGlyphs">BUILDER</text>
  <text class="tagline" x="41" y="251" font-size="32" textLength="524" lengthAdjust="spacingAndGlyphs">Residential and Commercial</text>

  <g class="brand-lockup">
    <rect x="42" y="372" width="30" height="30" fill="var(--brand)"/>
    <text class="brand-name" x="86" y="402" font-size="40" textLength="189" lengthAdjust="spacingAndGlyphs">Fernridge</text>
    <text class="brand-name" x="86" y="452" font-size="40" textLength="189" lengthAdjust="spacingAndGlyphs">Buildworks</text>
  </g>

  <g class="phone-icon" transform="translate(42 510)">
    <path class="icon-line" stroke-width="3.5"
          d="M8 4 L15 2 L21 13 L16 18 C19 25 24 30 31 33 L36 28 L41 34 L39 41 C22 42 6 26 8 4 Z"/>
  </g>
  <text class="phone-number" x="106" y="546" font-size="40" textLength="374" lengthAdjust="spacingAndGlyphs">027 584 9071</text>

  <g class="mail-icon" transform="translate(540 511)">
    <rect class="icon-line" stroke-width="2.2" x="0" y="0" width="17" height="13" rx="2"/>
    <path class="icon-line" stroke-width="2.2" d="M1 2 L8.5 8 L16 2"/>
  </g>
  <text class="web-contact" x="570" y="528" font-size="26" textLength="427" lengthAdjust="spacingAndGlyphs">info@fernridgebuildworks.co.nz</text>

  <g class="globe-icon" transform="translate(534 544)">
    <circle class="icon-line" stroke-width="2" cx="9" cy="9" r="8.5"/>
    <ellipse class="icon-line" stroke-width="1.6" cx="9" cy="9" rx="3.8" ry="8.5"/>
    <path class="icon-line" stroke-width="1.6" d="M0.5 9 H17.5 M2 4.5 H16 M2 13.5 H16"/>
  </g>
  <text class="web-contact" x="556" y="558" font-size="26" textLength="434" lengthAdjust="spacingAndGlyphs">www.fernridgebuildworks.co.nz</text>

  <rect class="badge-mark" x="1068" y="444" width="80" height="112" rx="3"/>
</svg>
</body>
</html>
```